Business Card design for construction company

I would like a business card design for a construction company - Harlow Constructions. I have attached the ai logo file for use. I would like the card to be very smart and clean and incorporate only white and the two colours in the logo. I would like the card to have two sides. One side can just have the logo, the other with the relevant information.

Target Market(s)

Building and Construction Clients

Industry/Entity Type

Business

Contact Information for Business Card

Name: Tom Pardoe
Company: Harlow Constructions Pty Limited
Address: 14 Mallee Crescent Carrow Vale 2093
Phone: 0427 531 068
Email: tomp@harlowbuild-example.com.au

Font styles to use
Serif
Sans Serif

Requirements
Must have
• Details noted above
• Logo as provided
• Colours as in logo
• Square edges
• A font that compliments the logo
Should not have
• Any colour other than white and those in logo
• Rounded edges

```html
<!DOCTYPE html>
<html lang="en">
<head>
<meta charset="utf-8">
<title>Harlow Constructions – Business Card</title>
<link rel="stylesheet" href="https://fonts.googleapis.com/css2?family=Open+Sans:wght@400;600;700&display=swap">
<style>
  :root {
    --backdrop: #222222;
    --card-white: #f4f4f4;
    --card-dark: #333333;
    --brand-blue: #4dbfea;
    --ink: #111111;
    --brand-grey: #5d5d5d;
  }
  * { margin: 0; padding: 0; box-sizing: border-box; }
  html, body {
    width: 1200px; height: 1000px; overflow: hidden;
    background: var(--backdrop);
    font-family: "Open Sans", Arial, sans-serif;
  }
  .card {
    position: absolute; left: 244px; width: 709px;
    box-shadow: 6px 8px 14px rgba(0,0,0,0.55);
  }
  .card--front { top: 52px; height: 425px; background: var(--card-white); }
  .card--back { top: 527px; height: 421px; background: var(--card-dark); }

  .name-block {
    position: absolute; left: 34px; top: 98px; width: 251px; height: 234px;
    background: var(--brand-blue);
  }
  .name-block__name {
    position: absolute; left: 14px; bottom: 38px;
    font-size: 36px; font-weight: 400; color: var(--ink);
    letter-spacing: 0.5px; white-space: nowrap;
  }
  .company-title {
    position: absolute; left: 310px; top: 105px;
    font-size: 23px; font-weight: 600; color: var(--ink); white-space: nowrap;
  }
  .company-rule {
    position: absolute; left: 306px; top: 144px; width: 343px; height: 2px;
    background: var(--brand-blue);
  }
  .contact { position: absolute; left: 314px; display: flex; align-items: center; }
  .contact--address { top: 164px; }
  .contact--phone { top: 221px; }
  .contact--email { top: 279px; }
  .contact__icon {
    width: 43px; height: 42px; background: var(--brand-blue);
    display: flex; align-items: center; justify-content: center;
  }
  .contact__text {
    margin-left: 17px; font-size: 15px; font-weight: 700; color: var(--ink); white-space: nowrap;
  }
  .contact--email .contact__text { font-weight: 600; color: #222; }

  .brand-mark {
    position: absolute; left: 0; right: 0; top: 0; bottom: 0;
    display: flex; align-items: center; justify-content: center;
  }
  .brand-mark__name {
    font-size: 38px; font-weight: 400; letter-spacing: 5px;
    color: var(--brand-grey); text-transform: uppercase; white-space: nowrap;
  }
</style>
</head>
<body>
  <section class="card card--front" aria-label="Business card front">
    <div class="name-block">
      <p class="name-block__name">TOM PARDOE</p>
    </div>
    <h1 class="company-title">Harlow Constructions Pty Limited</h1>
    <div class="company-rule"></div>

    <div class="contact contact--address">
      <div class="contact__icon">
        <svg width="22" height="30" viewBox="0 0 22 30" aria-hidden="true">
          <path d="M11 1C5.5 1 1.5 5 1.5 10.3 1.5 17 11 29 11 29s9.5-12 9.5-18.7C20.5 5 16.5 1 11 1z" fill="#111"/>
          <circle cx="11" cy="10.5" r="3.8" fill="#4dbfea"/>
        </svg>
      </div>
      <p class="contact__text">14 Mallee Crescent Carrow Vale 2093</p>
    </div>

    <div class="contact contact--phone">
      <div class="contact__icon">
        <svg width="24" height="26" viewBox="0 0 24 26" aria-hidden="true">
          <path d="M7 2 L3.5 4.5 C1.5 6 2 11 6 17 C10 23 15 25 17.5 23.8 L21 21.5 L17 16.5 L14 18.3 C12.5 17.5 10.5 15 9 12.5 C7.7 10 7.3 8.5 7.6 7.8 L10.5 5.8 Z" fill="none" stroke="#111" stroke-width="1.6" stroke-linejoin="round"/>
        </svg>
      </div>
      <p class="contact__text">0427 531 068</p>
    </div>

    <div class="contact contact--email">
      <div class="contact__icon">
        <svg width="26" height="26" viewBox="0 0 26 26" aria-hidden="true" fill="none" stroke="#111" stroke-width="1.4">
          <circle cx="13" cy="13" r="11"/>
          <ellipse cx="13" cy="13" rx="5" ry="11"/>
          <line x1="2" y1="13" x2="24" y2="13"/>
          <path d="M4 7.5 H22 M4 18.5 H22"/>
        </svg>
      </div>
      <p class="contact__text">tomp@harlowbuild-example.com.au</p>
    </div>
  </section>

  <section class="card card--back" aria-label="Business card back">
    <div class="brand-mark">
      <p class="brand-mark__name">Harlow Constructions</p>
    </div>
  </section>
</body>
</html>
```